tri fold logistics company FLYER and A4 COMPANY FLYER COVER and A4 company flyer

we need to design company tri fold brochure and A4 company flyer cover for us
our company website is www.harbingfreightways.com
pls design for us asap

ALSO OUR COMPANY NAME IS HARBING FREIGHTWAYS INC
NOT " HARBING FREIGHTWAYS, INC"

CAN YOU DESIGN THE COMPANY EMAIL SIGNATURE FOR US TOO

Target Market(s)

customer in U.S.

Industry/Entity Type

Freight Forwarding

Requirements
Must have
• company name and logo
• company name; HARBING FREIGHTWAYS INC
Nice to have
• international shipping map,

```html
<!DOCTYPE html>
<html lang="en">
<head>
<meta charset="utf-8">
<title>Harbing Freightways Inc — Tri-fold Brochure</title>
<link href="https://fonts.googleapis.com/css2?family=Raleway:wght@400;500;600;700;800&display=swap" rel="stylesheet">
<style>
:root{
  --backdrop:#3fa9db;
  --navy:#1d2a5c;
  --navy-deep:#151f47;
  --ink:#2a2f3f;
  --stripe:#c9d0e8;
  --paper:#ffffff;
  --muted:#d6dcef;
}
*{box-sizing:border-box;margin:0;padding:0}
html,body{width:1200px;height:1187px;overflow:hidden}
body{background:var(--backdrop);font-family:'Raleway',sans-serif;color:var(--ink)}
.brochure{position:absolute;left:45px;top:150px;width:1110px;height:880px;display:flex;box-shadow:0 18px 40px rgba(0,0,0,.25)}
.panel{width:370px;height:100%;position:relative;overflow:hidden}

/* left panel */
.panel--schedule{background:var(--paper);padding:30px 26px 20px}
.headline{font-size:15px;line-height:1.25;color:var(--navy);text-transform:uppercase;font-weight:500}
.headline strong{font-weight:800}
.headline .band{display:inline-block;background:var(--navy);color:#fff;font-weight:800;padding:2px 8px;margin-left:-8px}
.headline em{font-style:normal;font-weight:800}
.body-copy{font-size:8.2px;line-height:1.45;margin-top:12px}
.body-copy+.body-copy{margin-top:8px}
.schedule{width:100%;border-collapse:collapse;font-size:7.6px;margin-top:10px}
.schedule caption{background:var(--navy);color:#fff;font-weight:700;font-size:8.5px;text-transform:uppercase;padding:2px 0}
.schedule th{font-weight:700;font-style:italic;text-align:left;padding:1px 4px;font-size:7.2px}
.schedule td{padding:1.5px 4px;height:13px}
.schedule tbody tr:nth-child(odd){background:var(--stripe)}
.schedule td:nth-child(2),.schedule td:nth-child(3),.schedule th:nth-child(2),.schedule th:nth-child(3){text-align:center}

/* middle panel */
.panel--ocean{background:linear-gradient(180deg,var(--navy-deep),var(--navy) 60%);color:#fff;padding:40px 28px 0}
.section-title{font-size:17px;font-weight:600;text-transform:uppercase;letter-spacing:.2px}
.panel--ocean .body-copy{color:var(--muted);margin-top:14px}
.services-intro{font-size:12px;margin-top:24px;color:#fff}
.services{list-style:none;margin-top:14px}
.services li{display:flex;align-items:center;gap:16px;height:50px;font-size:11px;line-height:1.3}
.services svg{flex:0 0 50px}
.brand-tag{width:48px;height:26px;background:#fff;color:var(--navy);font-size:8px;font-weight:700;display:flex;align-items:center;justify-content:center;flex:0 0 48px;margin-right:2px}
.photo-warehouse{position:absolute;left:0;bottom:0;width:100%;height:340px;background:linear-gradient(160deg,#3b4a7c,#1a2548 55%,#0e1632)}

/* right panel */
.panel--air{background:var(--paper)}
.logo{display:flex;align-items:center;gap:10px;padding:28px 24px 0}
.logo-dot{width:34px;height:34px;border-radius:50%;background:var(--navy)}
.logo-name{font-size:14px;font-weight:700;color:var(--navy)}
.title-band{margin:26px 12px 0 10px;background:var(--navy);color:#fff;font-size:13px;font-weight:700;text-transform:uppercase;padding:6px 12px}
.panel--air .body-copy{padding:0 24px}
.photo-forklift{position:absolute;left:0;bottom:0;width:100%;height:470px;background:linear-gradient(135deg,#7a6a55,#3a3d4e 45%,#1f2438);clip-path:polygon(0 22%,100% 0,100% 100%,0 100%)}
.wedge{position:absolute;left:0;bottom:430px;width:100%;height:70px;background:var(--navy);clip-path:polygon(0 40%,100% 0,100% 0,0 100%)}
</style>
</head>
<body>
<main class="brochure">

  <section class="panel panel--schedule">
    <h2 class="headline"><strong>When your shipment is too big</strong><br>to fly but also pressing enough that<br><em>time is a significant factor,</em><br><span class="band">this service is for you.</span></h2>
    <p class="body-copy">We offer expedited service on our Pacific Arrow Express Service for full container loads from Shanghai, Ningbo, or Xiamen to select US markets. The expedited service is designed for customers looking for fast, industry leading, reliable transit times to the U.S. West Coast and select inland locations.</p>
    <p class="body-copy">Port to Rail Yard: Shanghai, Ningbo, or Xiamen to a variety of U.S. inland markets. Calder and Calder Logistics provide Expedited intermodal transportation of ocean containers from China to many major cities in the U.S. Midwest and East Coast.</p>

    <table class="schedule">
      <caption>From Shanghai</caption>
      <thead><tr><th>Destination City</th><th>Port to Port</th><th>Port to Railyard</th></tr></thead>
      <tbody>
        <tr><td>Long Beach</td><td>10 days</td><td></td></tr>
        <tr><td>Atlanta, GA</td><td></td><td>19 days</td></tr>
        <tr><td>Chicago, IL</td><td></td><td>18 days</td></tr>
        <tr><td>St. Louis, MO</td><td></td><td>19 days</td></tr>
        <tr><td>South Kearny, NJ</td><td></td><td>21 days</td></tr>
        <tr><td>Philadelphia, PA</td><td></td><td>24 days</td></tr>
        <tr><td>Memphis, TN</td><td></td><td>17 days</td></tr>
        <tr><td>Dallas, TX</td><td></td><td>17 days</td></tr>
        <tr><td>Houston, TX</td><td></td><td>18 days</td></tr>
        <tr><td>Honolulu</td><td>17 days</td><td>17 days</td></tr>
      </tbody>
    </table>
    <table class="schedule">
      <caption>From Ningbo</caption>
      <thead><tr><th>Destination City</th><th>Port to Port</th><th>Port to Railyard</th></tr></thead>
      <tbody>
        <tr><td>Long Beach</td><td>12 days</td><td></td></tr>
        <tr><td>Atlanta, GA</td><td></td><td>21 days</td></tr>
        <tr><td>Chicago, IL</td><td></td><td>20 days</td></tr>
        <tr><td>St. Louis, MO</td><td></td><td>21 days</td></tr>
        <tr><td>South Kearny, NJ</td><td></td><td>23 days</td></tr>
        <tr><td>Philadelphia, PA</td><td></td><td>22 days</td></tr>
        <tr><td>Memphis, TN</td><td></td><td>20 days</td></tr>
        <tr><td>Dallas, TX</td><td></td><td>20 days</td></tr>
        <tr><td>Houston, TX</td><td></td><td>20 days</td></tr>
        <tr><td>Honolulu</td><td>19 days</td><td>19 days</td></tr>
      </tbody>
    </table>
    <table class="schedule">
      <caption>From Xiamen</caption>
      <thead><tr><th>Destination City</th><th>Port to Port</th><th>Port to Railyard</th></tr></thead>
      <tbody>
        <tr><td>Long Beach</td><td>14 days</td><td></td></tr>
        <tr><td>Atlanta, GA</td><td></td><td>23 days</td></tr>
        <tr><td>Chicago, IL</td><td></td><td>22 days</td></tr>
        <tr><td>St. Louis, MO</td><td></td><td>23 days</td></tr>
        <tr><td>South Kearny, NJ</td><td></td><td>25 days</td></tr>
        <tr><td>Philadelphia, PA</td><td></td><td>24 days</td></tr>
        <tr><td>Memphis, TN</td><td></td><td>22 days</td></tr>
        <tr><td>Dallas, TX</td><td></td><td>22 days</td></tr>
        <tr><td>Houston, TX</td><td></td><td>22 days</td></tr>
        <tr><td>Honolulu</td><td>22 days</td><td></td></tr>
      </tbody>
    </table>
  </section>

  <section class="panel panel--ocean">
    <h2 class="section-title">Ocean Freight Services</h2>
    <p class="body-copy">We leverage our service contracts and strong network of more than 150 agents around the world. Effective communication and flawless execution make our ocean service one of the most reliable and professional services in its class. We are confident that we can make shipping arrangements that are a perfect fit for your needs.<br>We are an Ocean Transportation Intermediary (OTI) and Non-Vessel Operating Common Carrier (NVOCC) as licensed by the US Federal Maritime Commission. We are able to provide customs clearance at every US port under a national permit issued by the US Department of Homeland Security.</p>
    <p class="services-intro">Our most common ocean services include:</p>
    <ul class="services">
      <li><svg width="50" height="30" viewBox="0 0 50 30" fill="none" stroke="#fff" stroke-width="2"><rect x="2" y="4" width="34" height="14"/><path d="M36 10h8l4 6v4H2"/><circle cx="10" cy="24" r="3"/><circle cx="20" cy="24" r="3"/><circle cx="40" cy="24" r="3"/></svg><span>FCL (Full Container Load)<br>import and export</span></li>
      <li><svg width="50" height="30" viewBox="0 0 50 30" fill="none" stroke="#fff" stroke-width="2"><rect x="2" y="3" width="30" height="18" rx="2"/><path d="M32 9h8l6 7v5H32"/><circle cx="11" cy="24" r="3"/><circle cx="38" cy="24" r="3"/></svg><span>LCL (Less-than-Container Load)<br>import and export</span></li>
      <li><svg width="50" height="30" viewBox="0 0 50 30" fill="none" stroke="#fff" stroke-width="2"><path d="M8 2v20h22"/><path d="M20 4v10m-4-4 4 4 4-4"/><circle cx="12" cy="26" r="2"/><circle cx="26" cy="26" r="2"/></svg><span>General cargo or Dangerous Goods</span></li>
      <li><svg width="50" height="30" viewBox="0 0 50 30" fill="none" stroke="#fff" stroke-width="2"><path d="M6 8 18 2l14 6v16l-14 6-12-6z"/><path d="M6 8l12 6 14-6M18 14v16"/></svg><span>Personal effects, residential<br>pick up or delivery</span></li>
      <li><span class="brand-tag">marketly</span><span>Marketly shpt importing from China<br>or export Marketly shpt to UK</span></li>
    </ul>
    <div class="photo-warehouse" role="img" aria-label="Photo of palletised cartons stacked in a warehouse"></div>
  </section>

  <section class="panel panel--air">
    <div class="logo"><span class="logo-dot"></span><span class="logo-name">HARBING FREIGHTWAYS INC</span></div>
    <h2 class="title-band">Air Shipments and Expedited Delivery</h2>
    <p class="body-copy">Harbing Freightways provides international commercial air freight forwarding services. Our partners rely on our expert air freight agents to get it right the first time for your company's time sensitive and expedited international air freight shipments.</p>
    <p class="body-copy">We have strategic alliances with local and international air carriers which has enabled us to successfully grow our air services to offer competitive door-to-door delivery anywhere in the world. Our highly trained and dynamic operations team will guarantee efficient coordination of all your time sensitive air shipments. We're always focused on giving you every option to make sure your air cargo travels in the fastest and most cost-effective way possible. With our diverse delivery options we're confident that we can suit your needs!</p>
    <div class="wedge"></div>
    <div class="photo-forklift" role="img" aria-label="Photo of a forklift operator moving goods inside a warehouse with shelving"></div>
  </section>

</main>
</body>
</html>
```